Brelvanhomes42.com needs a website.

I'm looking for a website that offeres education and courses about the QZ home loan. This will teach people what they need to know about using the QZ loan. I need a website design that will allow the use of video, have sections to educate about the myths out there, use blue and red which are patriotic colors.

```html
<!DOCTYPE html>
<html lang="en">
<head>
<meta charset="utf-8">
<title>Contact Us – Brelvanhomes42.com</title>
<link href="https://fonts.googleapis.com/css2?family=Raleway:wght@600;700&family=Roboto:ital,wght@0,400;0,500;0,700;1,400&display=swap" rel="stylesheet">
<style>
:root{
  --navy:#0b1d51;
  --navy-2:#0e2362;
  --footer:#0c1f57;
  --blue:#0a62d6;
  --blue-light:#1a7ff0;
  --ink:#0f1b3d;
  --text:#3a4256;
  --field:#f4f5f7;
  --gold:#f5b400;
  --white:#fff;
  --muted-blue:#cfdcff;
}
*{box-sizing:border-box;margin:0;padding:0}
html,body{width:795px;height:1200px;overflow:hidden}
body{position:relative;font-family:"Roboto",sans-serif;background:var(--white);color:var(--text)}
.abs{position:absolute}
h1,h2,h3,h4{font-family:"Raleway",sans-serif}

/* top bar */
.topbar{left:0;top:0;width:795px;height:25px;background:var(--navy);color:var(--white);font-size:8px}
.topbar-item{top:8px;display:flex;align-items:center;gap:4px}
.topbar-sep{top:6px;width:1px;height:11px;background:var(--white)}
.social-dot{top:9px;width:8px;height:8px;border-radius:50%;background:var(--white)}

/* header */
.brand{left:8px;top:0;width:108px;height:66px;background:var(--blue);border-radius:0 0 8px 8px;display:flex;align-items:center;justify-content:center;z-index:2}
.brand-name{font-family:"Raleway",sans-serif;font-weight:700;font-size:9px;color:var(--white)}
.mainnav{left:0;top:25px;width:795px;height:52px;background:var(--white)}
.mainnav a{position:absolute;top:20px;font-family:"Raleway",sans-serif;font-weight:600;font-size:9.5px;color:var(--ink);text-decoration:none}
.mainnav a.current{color:var(--blue-light)}
.cart-badge{left:751px;top:42px;width:9px;height:9px;border-radius:50%;background:var(--blue-light);color:var(--white);font-size:5.5px;text-align:center;line-height:9px;font-weight:700}

/* hero */
.hero{left:0;top:77px;width:795px;height:166px;background:linear-gradient(90deg,#1b2e66 0%,#243a78 45%,#1c306b 100%)}
.hero-title{left:0;top:58px;width:795px;text-align:center;font-size:26px;font-weight:700;color:var(--white)}
.crumbs{left:0;top:98px;width:795px;text-align:center;font-size:8.5px;font-weight:700;color:var(--white);font-family:"Raleway",sans-serif}
.crumbs span{color:var(--blue-light)}

/* form */
.form-title{left:95px;top:305px;font-size:15px;font-weight:700;color:var(--ink)}
.form-intro{left:95px;top:336px;width:320px;font-size:8px;line-height:13.5px;color:var(--text)}
.field{background:var(--field);font-size:8px;font-style:italic;color:#3b4254}
.field span{position:absolute;left:11px}
.send-btn{left:95px;top:557px;width:120px;height:31px;background:var(--blue);color:var(--white);font-family:"Raleway",sans-serif;font-weight:700;font-size:8.5px;display:flex;align-items:center;justify-content:center;gap:6px}

/* contact info */
.info{left:509px;top:305px;width:191px;height:294px;background:var(--navy-2);color:var(--white)}
.info h3{position:absolute;left:21px;top:27px;font-size:15px;font-weight:700}
.info-icon{position:absolute;left:21px;width:31px;height:31px;border-radius:50%;background:var(--white);display:flex;align-items:center;justify-content:center}
.info-label{position:absolute;left:62px;font-family:"Raleway",sans-serif;font-weight:700;font-size:8.5px}
.info-value{position:absolute;left:62px;font-size:8px;line-height:12.5px;color:#dfe6fb}
.follow{position:absolute;left:21px;top:223px;font-family:"Raleway",sans-serif;font-weight:700;font-size:9px}
.follow-dot{position:absolute;top:246px;width:21px;height:21px;border-radius:50%;background:#1a3074}
.follow-dot::after{content:"";position:absolute;left:8px;top:8px;width:5px;height:5px;border-radius:50%;background:var(--white)}

/* map */
.map{left:0;top:661px;width:795px;height:259px;background:linear-gradient(135deg,#bfe0c4 0%,#d9ecd6 45%,#e6eee6 60%,#a9cdee 100%)}

/* footer */
.footer{left:0;top:920px;width:795px;height:280px;background:var(--footer);color:var(--white)}
.footer h4{position:absolute;top:48px;font-size:11.5px;font-weight:700}
.footer-links a{position:absolute;font-size:8px;color:var(--white);text-decoration:none}
.footer-about{position:absolute;left:95px;top:81px;width:135px;font-size:8px;line-height:13.5px;color:var(--muted-blue)}
.sub-email{position:absolute;left:95px;top:159px;width:108px;height:29px;background:var(--white);font-size:8px;color:#6b7280;padding:11px 0 0 13px}
.sub-btn{position:absolute;left:203px;top:159px;width:32px;height:29px;background:var(--blue);display:flex;align-items:center;justify-content:center}
.fi-row{position:absolute;left:560px;display:flex;gap:7px;font-size:8px;align-items:flex-start;line-height:14px}
.fsoc{position:absolute;top:158px;width:20px;height:20px;border-radius:50%;background:#1a3074}
.fsoc::after{content:"";position:absolute;left:7.5px;top:7.5px;width:5px;height:5px;border-radius:50%;background:var(--white)}
.divider{position:absolute;left:95px;top:235px;width:605px;height:1px;background:#233777}
.copy{position:absolute;left:95px;top:253px;font-size:8px}
.legal{position:absolute;right:95px;top:253px;font-size:8px;display:flex;gap:10px}
.to-top{left:762px;top:1132px;width:25px;height:26px;background:var(--blue);display:flex;align-items:center;justify-content:center}
</style>
</head>
<body>

<!-- top bar -->
<div class="abs topbar">
  <div class="abs topbar-item" style="left:152px">
    <svg width="8" height="9" viewBox="0 0 10 12"><path d="M5 11S1 6.8 1 4.3a4 4 0 0 1 8 0C9 6.8 5 11 5 11z" fill="none" stroke="var(--gold)" stroke-width="1.3"/><circle cx="5" cy="4.3" r="1.3" fill="none" stroke="var(--gold)" stroke-width="1.1"/></svg>
    Address : K7PM+4Q2 Ohio, USA
  </div>
  <div class="abs topbar-sep" style="left:310px"></div>
  <div class="abs topbar-item" style="left:325px">
    <svg width="9" height="9" viewBox="0 0 10 10"><circle cx="5" cy="5" r="4.2" fill="none" stroke="var(--gold)" stroke-width="1.1"/><path d="M5 2.6V5l1.6 1" fill="none" stroke="var(--gold)" stroke-width="1.1"/></svg>
    Working : Monday - Friday, 9:Am - 5:Pm
  </div>
  <div class="abs topbar-item" style="left:621px">
    <svg width="8" height="9" viewBox="0 0 10 11"><circle cx="5" cy="3.3" r="2.4" fill="none" stroke="var(--gold)" stroke-width="1.1"/><path d="M1 10.5a4 4 0 0 1 8 0z" fill="none" stroke="var(--gold)" stroke-width="1.1"/></svg>
    Login/ Register
  </div>
  <div class="abs topbar-sep" style="left:706px"></div>
  <div class="abs social-dot" style="left:725px"></div>
  <div class="abs social-dot" style="left:742px"></div>
  <div class="abs social-dot" style="left:760px"></div>
  <div class="abs social-dot" style="left:778px"></div>
</div>

<!-- header -->
<div class="abs brand"><span class="brand-name">Brelvanhomes42.com</span></div>
<nav class="abs mainnav">
  <a style="left:247px">Home</a>
  <a style="left:294px">About Us</a>
  <a style="left:355px">Courses</a>
  <a style="left:412px">Video Library</a>
  <a style="left:491px">Blog</a>
  <a class="current" style="left:533px">Contact</a>
  <svg class="abs" style="left:713px;top:20px" width="11" height="11" viewBox="0 0 12 12"><circle cx="5" cy="5" r="4" fill="none" stroke="var(--ink)" stroke-width="1.3"/><path d="M8 8l3.3 3.3" stroke="var(--ink)" stroke-width="1.3"/></svg>
  <svg class="abs" style="left:740px;top:19px" width="11" height="12" viewBox="0 0 11 12"><path d="M1.5 3.5h8l-.6 7.5H2.1z" fill="none" stroke="var(--ink)" stroke-width="1.2"/><path d="M3.5 5V2.8a2 2 0 0 1 4 0V5" fill="none" stroke="var(--ink)" stroke-width="1.1"/></svg>
  <svg class="abs" style="left:774px;top:21px" width="14" height="10" viewBox="0 0 14 10"><path d="M0 1h14M4 5h10M0 9h14" stroke="var(--blue-light)" stroke-width="1.3"/></svg>
</nav>
<div class="abs cart-badge">0</div>

<!-- hero -->
<section class="abs hero" role="img" aria-label="Photo of people studying together, tinted dark blue">
  <h1 class="abs hero-title">Contact Us</h1>
  <div class="abs crumbs">Home &nbsp;/ <span>Contact Us</span></div>
</section>

<!-- form -->
<h2 class="abs form-title">Free Massage Us</h2>
<p class="abs form-intro">Pellentesque Felis Cursus. Proin Lacus Magna, Lobortis Vel Quam Ac, Dignissim Dapibus Odio. Pellentesque Vulputate</p>
<div class="abs field" style="left:95px;top:385px;width:168px;height:61px"><span style="top:11px">Your Name</span><span style="top:42px">Your Phone</span></div>
<div class="abs field" style="left:273px;top:385px;width:168px;height:61px"><span style="top:11px;left:11px">Email address</span><span style="top:42px">Subject</span></div>
<div class="abs field" style="left:95px;top:457px;width:346px;height:77px"><span style="top:11px;left:8px">Message</span></div>
<div class="abs send-btn">SEND MESSAGE
  <svg width="11" height="8" viewBox="0 0 11 8"><path d="M0 4h10M7 1l3 3-3 3" fill="none" stroke="#fff" stroke-width="1.2"/></svg>
</div>

<!-- contact info -->
<aside class="abs info">
  <h3>Contact Info</h3>
  <div class="info-icon" style="top:63px"><svg width="10" height="12" viewBox="0 0 10 12"><path d="M5 11S1 6.8 1 4.3a4 4 0 0 1 8 0C9 6.8 5 11 5 11z" fill="none" stroke="var(--gold)" stroke-width="1.1"/><circle cx="5" cy="4.3" r="1.3" fill="none" stroke="var(--gold)" stroke-width="1"/></svg></div>
  <div class="info-label" style="top:65px">Location</div>
  <div class="info-value" style="top:81px">5HR3+218 Ohio,<br>United States</div>
  <div class="info-icon" style="top:122px"><svg width="11" height="9" viewBox="0 0 11 9"><rect x=".6" y=".6" width="9.8" height="7.8" rx="1" fill="none" stroke="var(--blue)" stroke-width="1"/><path d="M.8 1.2l4.7 3.4 4.7-3.4" fill="none" stroke="var(--blue)" stroke-width="1"/></svg></div>
  <div class="info-label" style="top:124px">Email Address</div>
  <div class="info-value" style="top:141px">info@brelvanhomes42.com</div>
  <div class="info-icon" style="top:169px"><svg width="11" height="11" viewBox="0 0 12 12"><path d="M2 1l2.3.2.9 2.4-1.4 1a7 7 0 0 0 3.6 3.6l1-1.4 2.4.9.2 2.3C7 11 1 5 2 1z" fill="none" stroke="var(--blue)" stroke-width="1"/></svg></div>
  <div class="info-label" style="top:171px">Phone No:</div>
  <div class="info-value" style="top:187px">(+1) 418 302 774</div>
  <div class="follow">Follow Us</div>
  <div class="follow-dot" style="left:21px"></div>
  <div class="follow-dot" style="left:47px"></div>
  <div class="follow-dot" style="left:72px"></div>
  <div class="follow-dot" style="left:98px"></div>
</aside>

<!-- map -->
<div class="abs map" role="img" aria-label="Embedded location map"></div>

<!-- footer -->
<footer class="abs footer">
  <h4 style="left:95px">Get Started</h4>
  <h4 style="left:250px">Our Courses</h4>
  <h4 style="left:405px">Company</h4>
  <h4 style="left:560px">Infomation</h4>

  <p class="footer-about">Integer Gravida Posuere Lacus Et Suscipit. Pellentesque Sed Ipsum Sollicitudin, Fermentum Nibh Elementum, Dignissim Leo. In Hac Habitasse Platea Dictumst.</p>
  <div class="sub-email">Email Address</div>
  <div class="sub-btn"><svg width="9" height="9" viewBox="0 0 10 10"><path d="M9 1L1 5.5 5 6l1 3.5z" fill="#fff"/></svg></div>

  <div class="footer-links">
    <a style="left:250px;top:83px">Loan Basics</a>
    <a style="left:250px;top:106px">Eligibility Criteria</a>
    <a style="left:250px;top:129px">QZ Appraisals / LAPP</a>
    <a style="left:250px;top:152px">Credit Underwriting</a>
    <a style="left:250px;top:175px">Loan Processing Steps</a>
    <a style="left:405px;top:83px">About Us</a>
    <a style="left:405px;top:106px">Become An Instructor</a>
    <a style="left:405px;top:129px">Student Registration</a>
    <a style="left:405px;top:152px">FAQs</a>
    <a style="left:405px;top:175px">Contact Us</a>
  </div>

  <div class="fi-row" style="top:82px"><svg width="13" height="13" viewBox="0 0 12 12"><path d="M2 1l2.3.2.9 2.4-1.4 1a7 7 0 0 0 3.6 3.6l1-1.4 2.4.9.2 2.3C7 11 1 5 2 1z" fill="none" stroke="var(--blue-light)" stroke-width=".9"/></svg>(+1) 418 302 774</div>
  <div class="fi-row" style="top:103px"><svg width="13" height="13" viewBox="0 0 11 9"><rect x=".6" y=".6" width="9.8" height="7.8" rx="1" fill="none" stroke="var(--blue-light)" stroke-width=".9"/><path d="M.8 1.2l4.7 3.4 4.7-3.4" fill="none" stroke="var(--blue-light)" stroke-width=".9"/></svg>info@brelvanhomes42.com</div>
  <div class="fi-row" style="top:124px"><svg width="13" height="14" viewBox="0 0 10 12"><path d="M5 11S1 6.8 1 4.3a4 4 0 0 1 8 0C9 6.8 5 11 5 11z" fill="none" stroke="var(--blue-light)" stroke-width=".9"/><circle cx="5" cy="4.3" r="1.3" fill="none" stroke="var(--blue-light)" stroke-width=".9"/></svg>5HR3+218 Ohio,<br>United States</div>

  <div class="fsoc" style="left:561px"></div>
  <div class="fsoc" style="left:587px"></div>
  <div class="fsoc" style="left:613px"></div>
  <div class="fsoc" style="left:640px"></div>

  <div class="divider"></div>
  <div class="copy">Copyright © 2023 Brelvan Homes 42. All Rights Reserved.</div>
  <div class="legal"><span>Support</span><span>|</span><span>Privacy</span><span>|</span><span>Policy</span></div>
</footer>
<div class="abs to-top"><svg width="8" height="5" viewBox="0 0 8 5"><path d="M1 4l3-3 3 3" fill="none" stroke="#fff" stroke-width="1.2"/></svg></div>

</body>
</html>
```